The Lanternfield Evenings - Concert Series Website Design

I've recently decided to launch a concert series in my living room and would love a website to use to promote the series. I'm looking for a simple Wix design that I could take over once it's complete. I'll provide the logo for which I'd like the website to utilize the color scheme.

Target Market(s)

Music lovers in Denver

Industry/Entity Type

Music

Coding

Coded - Design and coding required

Number of Pages Required

2 page

Font styles to use
Script

Requirements
Must have
• 2 pages - one for concert goers to see the schedule and rsvp, and one for artists about the booking process

```html
<!DOCTYPE html>
<html lang="en">
<head>
<meta charset="utf-8">
<title>The Lanternfield Evenings</title>
<link href="https://fonts.googleapis.com/css2?family=Great+Vibes&family=Poppins:wght@400;500;600&display=swap" rel="stylesheet">
<style>
:root{
  --cream:#fff8ef;
  --plum:#2b0a45;
  --plum-deep:#1f0735;
  --plum-mid:#4a1560;
  --berry:#6e2458;
  --amber:#f6b35c;
  --coral:#e2777a;
  --ink:#1c1424;
  --white:#ffffff;
  --line:#e6ddd5;
  --script:"Great Vibes",cursive;
  --sans:"Poppins",sans-serif;
}
*{box-sizing:border-box;margin:0;padding:0}
html,body{width:1200px;height:3260px;overflow:hidden}
body{position:relative;background:var(--cream);font-family:var(--sans);color:var(--ink)}
.abs{position:absolute}
.script{font-family:var(--script);font-weight:400}

/* top bar */
.topbar{left:0;top:0;width:1200px;height:32px;background:linear-gradient(90deg,var(--plum),var(--berry));color:var(--white);font-size:13px}
.topbar .socials{left:140px;top:9px;display:flex;gap:12px}
.topbar .socials span{width:13px;height:13px;border-radius:50%;background:var(--white);display:block}
.topbar .contact{right:140px;top:7px;display:flex;gap:28px;align-items:center}
.topbar .contact div{display:flex;gap:6px;align-items:center}

/* header */
.header{left:0;top:32px;width:1200px;height:79px;background:var(--cream)}
.brand{display:flex;align-items:center;gap:10px}
.brand .mark{width:40px;height:40px;border-radius:50%;background:var(--berry)}
.brand .name{font-family:var(--sans);font-weight:500;color:var(--berry);font-size:17px;line-height:1.05;text-transform:uppercase}
.header .brand{left:142px;top:18px}
.nav{right:142px;top:19px;display:flex;align-items:center;gap:28px;font-size:13px;font-weight:500;color:var(--plum);text-transform:uppercase}
.btn{display:inline-flex;align-items:center;justify-content:center;font-family:var(--sans);font-weight:500;font-size:13px;text-transform:uppercase;border-radius:6px;height:46px;padding:0 16px;white-space:nowrap}
.btn-plum{background:linear-gradient(90deg,var(--plum),var(--berry));color:var(--white)}
.btn-sun{background:linear-gradient(90deg,var(--amber),var(--coral));color:var(--plum)}
.btn-ghost{border:1.5px solid var(--white);color:var(--white)}
.nav .btn{height:42px}

/* hero */
.hero{left:0;top:111px;width:1200px;height:583px}
.hero-copy{left:63px;top:118px;color:var(--white)}
.eyebrow{font-size:17px;font-weight:500;text-transform:uppercase;letter-spacing:.3px}
.hero-title{font-size:82px;line-height:.86;margin-top:14px}
.hero-sub{font-size:15px;margin-top:16px}
.hero-ctas{display:flex;gap:12px;margin-top:18px}

/* about */
.about-photo{left:142px;top:732px}
.about-ring{left:362px;top:913px;width:232px;height:232px;border-radius:50%;background:var(--cream);padding:9px}
.about-ring div{width:100%;height:100%;border-radius:50%;background:radial-gradient(circle at 50% 40%,#b77a4c,#4a2a22 70%,#2a1714)}
.about-text{left:642px;top:754px;width:420px}
.label{font-size:14px;font-weight:500;color:var(--berry);text-transform:uppercase}
.about-text h2{font-size:44px;color:var(--plum);line-height:1.1;margin-top:2px;white-space:nowrap}
.rule{width:68px;height:4px;border-radius:2px;background:linear-gradient(90deg,var(--amber),var(--coral))}
.about-text .rule{margin-top:6px}
.about-text p{font-size:13px;line-height:22.5px;margin-top:18px;color:var(--ink)}
.about-text p + p{margin-top:6px}
.about-text .btn{margin-top:26px}

/* features */
.card{top:1266px;width:212px;height:177px;background:var(--white);border-radius:16px;box-shadow:0 6px 22px rgba(60,20,70,.10);text-align:center}
.badge{position:absolute;left:63px;top:-41px;width:86px;height:96px}
.card h3{font-family:var(--script);font-weight:400;font-size:29px;color:var(--plum);margin-top:68px;white-space:nowrap}
.card p{font-size:13px;line-height:23px;margin-top:2px;padding:0 10px}

/* quote */
.quote{left:0;top:1537px;width:1200px;height:296px;background:linear-gradient(120deg,var(--plum-deep),var(--berry));color:var(--white);text-align:center}
.quote svg{position:absolute;left:570px;top:61px}
.quote p{position:absolute;left:0;top:118px;width:1200px;font-size:47px;line-height:56px}

/* join */
.join{left:0;top:1912px;width:1200px;text-align:center}
.join .label{font-size:14px}
.join h2{font-size:56px;color:var(--plum);line-height:1;margin-top:4px}
.join .rule{margin:8px auto 0}
.join p{font-size:13px;line-height:23px;margin-top:10px}
.field{background:var(--white);border:1px solid var(--line);border-radius:6px;box-shadow:0 2px 8px rgba(0,0,0,.04);display:flex;align-items:flex-start;padding-top:17px;font-size:12px;color:#8a8390}
.field svg{margin:0 12px 0 12px}
.field .sep{width:1px;height:18px;background:var(--line);margin-right:12px;margin-top:-2px}
.submit{left:292px;top:2343px;width:616px;height:54px;border-radius:6px;font-size:13px;font-weight:600}

/* cta */
.cta-left{left:0;top:2493px;width:611px;height:415px;background:linear-gradient(120deg,var(--amber),var(--coral))}
.cta-photo{left:611px;top:2493px;width:589px;height:415px;background:radial-gradient(ellipse at 50% 40%,#8a4a2c,#3e2218 60%,#1d0e10)}
.cta-copy{left:141px;top:2540px;width:470px;color:var(--white)}
.cta-copy h2{font-size:46px;line-height:1.2;white-space:nowrap}
.cta-copy p{font-size:15px;line-height:24px;margin-top:10px;width:380px}
.cta-copy .btns{display:flex;gap:12px;margin-top:32px}
.cta-copy .btn-ghost{border-color:rgba(255,255,255,.8)}

/* footer */
.footer{left:0;top:2908px;width:1200px;height:352px;background:var(--plum-deep);color:var(--white)}
.footer .brand{position:absolute;left:484px;top:46px}
.footer .brand .mark{width:64px;height:64px;background:var(--coral)}
.footer .brand .name{color:var(--white);font-size:26px}
.f-socials{position:absolute;left:527px;top:138px;display:flex;gap:10px}
.f-socials span{width:29px;height:29px;border-radius:50%;border:1px solid rgba(255,255,255,.7);display:flex;align-items:center;justify-content:center}
.f-socials span i{width:9px;height:9px;border-radius:50%;background:var(--white);display:block}
.f-socials span.on{background:linear-gradient(135deg,var(--amber),var(--coral));border:none}
.f-line{position:absolute;left:142px;width:916px;height:1px;background:rgba(255,255,255,.18)}
.f-item{position:absolute;top:227px;display:flex;align-items:center;gap:14px;font-size:13px;line-height:20px}
.f-item .ic{width:42px;height:42px;border-radius:50%;background:var(--white);display:flex;align-items:center;justify-content:center}
.copy{position:absolute;left:0;top:313px;width:1200px;text-align:center;font-size:13px}
</style>
</head>
<body>

<div class="abs topbar">
  <div class="abs socials"><span></span><span></span><span></span><span></span></div>
  <div class="abs contact">
    <div><svg width="14" height="10" viewBox="0 0 14 10"><rect x=".5" y=".5" width="13" height="9" fill="none" stroke="#fff"/><path d="M.5 .5 7 6l6.5-5.5" fill="none" stroke="#fff"/></svg>Email: hello@lanternfieldevenings.com</div>
    <div><svg width="12" height="12" viewBox="0 0 24 24"><path d="M6.6 10.8a15 15 0 0 0 6.6 6.6l2.2-2.2c.3-.3.7-.4 1-.2 1.1.4 2.3.6 3.6.6.6 0 1 .4 1 1V20c0 .6-.4 1-1 1A17 17 0 0 1 3 4c0-.6.4-1 1-1h3.5c.6 0 1 .4 1 1 0 1.3.2 2.5.6 3.6.1.3 0 .7-.2 1z" fill="#fff"/></svg>Phone: 303-555-0148</div>
  </div>
</div>

<header class="abs header">
  <div class="abs brand"><span class="mark"></span><span class="name">The<br>Lanternfield<br>Evenings</span></div>
  <nav class="abs nav"><span>Home</span><span>About Us</span><span class="btn btn-plum">Contact Us</span></nav>
</header>

<section class="abs hero">
  <svg class="abs" style="left:0;top:0" width="1200" height="583" viewBox="0 0 1200 583" role="img" aria-label="Photo of musicians playing guitar, cajon and upright bass to a seated audience in a warmly lit living room">
    <defs>
      <linearGradient id="heroFill" x1="0" y1="0" x2="1" y2="0.4">
        <stop offset="0" stop-color="#251410"/>
        <stop offset=".45" stop-color="#5a2e22"/>
        <stop offset=".75" stop-color="#7a3a3a"/>
        <stop offset="1" stop-color="#3a1a1c"/>
      </linearGradient>
    </defs>
    <path d="M0 0H1200V430Q1192 492 1114 509L608 583L100 509Q8 492 0 430Z" fill="url(#heroFill)"/>
  </svg>
  <div class="abs hero-copy">
    <div class="eyebrow">A Living Room Concert Series</div>
    <h1 class="script hero-title">The Lanternfield<br>Evenings</h1>
    <div class="hero-sub">Intimate Concerts In Denver's North End</div>
    <div class="hero-ctas"><span class="btn btn-sun">Discover More</span><span class="btn btn-ghost">Stay Informed</span></div>
  </div>
</section>

<svg class="abs about-photo" width="334" height="420" viewBox="0 0 334 420" role="img" aria-label="Photo of a woman singing into a microphone with a drummer behind her">
  <defs><linearGradient id="aboutFill" x1="0" y1="0" x2="1" y2="1"><stop offset="0" stop-color="#d8b08a"/><stop offset=".5" stop-color="#9a6a4e"/><stop offset="1" stop-color="#2e1c18"/></linearGradient></defs>
  <path d="M0 0H334V300L164 420L30 345Q0 325 0 290Z" fill="url(#aboutFill)"/>
</svg>
<div class="abs about-ring" role="img" aria-label="Photo of a small band playing to guests in a living room"><div></div></div>

<section class="abs about-text">
  <div class="label">About Us</div>
  <h2 class="script">The Lanternfield Evenings</h2>
  <div class="rule"></div>
  <p>I'm Delighted To Announce <strong>The Launch Of The Lanternfield Evenings: Intimate Concerts In Denver's North End.</strong></p>
  <p>Inspired By The Quiet Radiance That Settles Over The Mountains At Dusk, The Lanternfield Evenings Is A New Living Room Concert Series Devoted To Attentive Listening, Artistic Depth, And Shared Musical Experience. Hosted In My Home In Denver's North End Of Central Park, These Gatherings Will Bring Folks Together For Evenings Of Warmth, Nuance, And Connection.</p>
  <span class="btn btn-plum" style="width:119px">Read More</span>
</section>

<div class="abs card" style="left:142px">
  <svg class="badge" viewBox="0 0 86 96"><path d="M0 4Q43-4 86 4V52Q86 80 43 96Q0 80 0 52Z" fill="var(--plum-mid)"/>
    <g fill="#fff"><circle cx="43" cy="34" r="6"/><circle cx="28" cy="37" r="5"/><circle cx="58" cy="37" r="5"/><path d="M32 56a11 10 0 0 1 22 0z"/><path d="M18 56a10 9 0 0 1 15-7 14 14 0 0 0-2 7z"/><path d="M68 56a10 9 0 0 0-15-7 14 14 0 0 1 2 7z"/></g></svg>
  <h3>25–40 Guests</h3>
  <p>Tiny Gatherings, Huge Intimacy. Every Note Shared.</p>
</div>
<div class="abs card" style="left:376px">
  <svg class="badge" viewBox="0 0 86 96"><defs><linearGradient id="sunB" x1="0" y1="0" x2="0" y2="1"><stop offset="0" stop-color="#f6b35c"/><stop offset="1" stop-color="#e2777a"/></linearGradient></defs><path d="M0 4Q43-4 86 4V52Q86 80 43 96Q0 80 0 52Z" fill="url(#sunB)"/>
    <path d="M43 22a13 13 0 0 0-13 13c0 10 13 24 13 24s13-14 13-24a13 13 0 0 0-13-13z" fill="none" stroke="#fff" stroke-width="3.5"/><circle cx="43" cy="35" r="4.5" fill="#fff"/><path d="M30 63h26" stroke="#fff" stroke-width="3"/></svg>
  <h3>North End · Denver</h3>
  <p>Hosted In My Home In Central Park — Cozy &amp; Welcoming.</p>
</div>
<div class="abs card" style="left:611px">
  <svg class="badge" viewBox="0 0 86 96"><path d="M0 4Q43-4 86 4V52Q86 80 43 96Q0 80 0 52Z" fill="var(--plum-mid)"/>
    <g fill="#fff"><path d="M32 28l22-5v5l-18 4v22h-4z"/><ellipse cx="29" cy="55" rx="6" ry="5"/><path d="M50 24h4v26h-4z"/><ellipse cx="48" cy="51" rx="6" ry="5"/></g></svg>
  <h3>Attentive Listening</h3>
  <p>Concerts Designed For Depth, Not Distraction.</p>
</div>
<div class="abs card" style="left:846px">
  <svg class="badge" viewBox="0 0 86 96"><path d="M0 4Q43-4 86 4V52Q86 80 43 96Q0 80 0 52Z" fill="url(#sunB)"/>
    <rect x="24" y="26" width="38" height="34" rx="4" fill="none" stroke="#fff" stroke-width="3.5"/><path d="M24 35h38M33 21v9M53 21v9" stroke="#fff" stroke-width="3.5"/>
    <g fill="#fff"><rect x="30" y="40" width="6" height="5"/><rect x="40" y="40" width="6" height="5"/><rect x="50" y="40" width="6" height="5"/><rect x="30" y="49" width="6" height="5"/><rect x="40" y="49" width="6" height="5"/><rect x="50" y="49" width="6" height="5"/></g></svg>
  <h3>Inaugural Date</h3>
  <p>Artist Lineup &amp; First Concert Announced Soon!</p>
</div>

<section class="abs quote">
  <svg width="60" height="46" viewBox="0 0 60 46"><defs><linearGradient id="qG" x1="0" y1="0" x2="1" y2="1"><stop offset="0" stop-color="#f6b35c"/><stop offset="1" stop-color="#e2777a"/></linearGradient></defs>
    <path d="M4 0h20a4 4 0 0 1 4 4v16c0 14-8 24-20 26l-2-6c6-2 10-7 10-14H4a4 4 0 0 1-4-4V4a4 4 0 0 1 4-4zM36 0h20a4 4 0 0 1 4 4v16c0 14-8 24-20 26l-2-6c6-2 10-7 10-14h-12a4 4 0 0 1-4-4V4a4 4 0 0 1 4-4z" fill="url(#qG)"/></svg>
  <p class="script">Extraordinary music does not require a grand hall. It requires<br>space, intention, and a community willing to listen.</p>
</section>

<section class="abs join">
  <div class="label">Stay Connected</div>
  <h2 class="script">Join Us</h2>
  <div class="rule"></div>
  <p>Our Inaugural Concert Date And Artist Lineup Will Be Announced Soon. Seating<br>Will Be Limited, And Reservations Will Be Required.</p>
</section>

<div class="abs field" style="left:292px;top:2076px;width:300px;height:53px"><svg width="14" height="14" viewBox="0 0 14 14" fill="none" stroke="#a8a1ad"><circle cx="7" cy="4.5" r="3"/><path d="M1.5 13.5a5.5 5 0 0 1 11 0"/></svg><span class="sep"></span>First Name</div>
<div class="abs field" style="left:608px;top:2076px;width:300px;height:53px"><svg width="14" height="14" viewBox="0 0 14 14" fill="none" stroke="#a8a1ad"><circle cx="7" cy="4.5" r="3"/><path d="M1.5 13.5a5.5 5 0 0 1 11 0"/></svg><span class="sep"></span>Last Name</div>
<div class="abs field" style="left:292px;top:2145px;width:300px;height:53px"><svg width="14" height="14" viewBox="0 0 14 14" fill="none" stroke="#a8a1ad"><rect x="1" y="3" width="12" height="9" rx="1"/><path d="M1 4l6 4 6-4"/></svg><span class="sep"></span>Your Email</div>
<div class="abs field" style="left:608px;top:2145px;width:300px;height:53px"><svg width="14" height="14" viewBox="0 0 24 24" fill="none" stroke="#a8a1ad" stroke-width="1.6"><path d="M6.6 10.8a15 15 0 0 0 6.6 6.6l2.2-2.2c.3-.3.7-.4 1-.2 1.1.4 2.3.6 3.6.6.6 0 1 .4 1 1V20c0 .6-.4 1-1 1A17 17 0 0 1 3 4c0-.6.4-1 1-1h3.5c.6 0 1 .4 1 1 0 1.3.2 2.5.6 3.6.1.3 0 .7-.2 1z"/></svg><span class="sep"></span>Phone</div>
<div class="abs field" style="left:292px;top:2213px;width:616px;height:108px"><svg width="14" height="14" viewBox="0 0 14 14" fill="none" stroke="#a8a1ad"><path d="M7 1.5c3.3 0 6 2.1 6 4.8S10.3 11 7 11c-.8 0-1.5-.1-2.2-.3L1.5 12.5l1-2.6C1.6 9 1 7.7 1 6.3 1 3.6 3.7 1.5 7 1.5z"/></svg><span class="sep"></span>Your Message</div>
<div class="abs btn btn-plum submit">Submit Now</div>

<section class="abs cta-left"></section>
<div class="abs cta-photo" role="img" aria-label="Photo of a singer and band performing to a crowd in a dim, lamp-lit living room"></div>
<div class="abs cta-copy">
  <h2 class="script">The Lanternfield Evenings</h2>
  <p>Our Inaugural Concert Date And Artist Lineup Will Be Announced Soon. Seating Will Be Limited, And Reservations Will Be Required. I Hope You'll Join Us As We Begin This New Chapter Together.</p>
  <div class="btns"><span class="btn btn-plum">Discover More</span><span class="btn btn-ghost">Stay Informed</span></div>
</div>

<footer class="abs footer">
  <div class="brand"><span class="mark"></span><span class="name">The<br>Lanternfield<br>Evenings</span></div>
  <div class="f-socials"><span class="on"><i></i></span><span><i></i></span><span><i></i></span><span><i></i></span></div>
  <div class="f-line" style="top:201px"></div>
  <div class="f-item" style="left:142px"><span class="ic"><svg width="16" height="20" viewBox="0 0 16 20"><path d="M8 0a8 8 0 0 0-8 8c0 6 8 12 8 12s8-6 8-12a8 8 0 0 0-8-8z" fill="#1f0735"/><circle cx="8" cy="8" r="3" fill="#fff"/></svg></span><span>Intimate Concerts In<br>Denver's North End</span></div>
  <div class="f-item" style="left:527px"><span class="ic"><svg width="18" height="18" viewBox="0 0 24 24"><path d="M6.6 10.8a15 15 0 0 0 6.6 6.6l2.2-2.2c.3-.3.7-.4 1-.2 1.1.4 2.3.6 3.6.6.6 0 1 .4 1 1V20c0 .6-.4 1-1 1A17 17 0 0 1 3 4c0-.6.4-1 1-1h3.5c.6 0 1 .4 1 1 0 1.3.2 2.5.6 3.6.1.3 0 .7-.2 1z" fill="#1f0735"/></svg></span><span>Phone<br>303-555-0148</span></div>
  <div class="f-item" style="left:868px"><span class="ic"><svg width="20" height="14" viewBox="0 0 20 14"><rect width="20" height="14" rx="2" fill="#1f0735"/><path d="M1 1l9 7 9-7" fill="none" stroke="#fff" stroke-width="1.5"/></svg></span><span>Email:<br>hello@lanternfieldevenings.com</span></div>
  <div class="f-line" style="top:289px"></div>
  <div class="copy">© 2026 The Lanternfield Evenings. All Rights Reserved.</div>
</footer>

</body>
</html>
```